Need a Facebook image for childcare advertisement

We are after a design for Facebook advertisement for childcare and kindergarten centre enrolments for 2023.

I have attached a previous flyer that we have in pdf format. The new logo is also attached with this brief.

All other information is still current as per the attached flyer.

You can use same colours as per attached flyer. I will also attached some stock images that you can select to use for the design.

our website for your reference:

https://tallowmere-vale.com.au

```html
<!DOCTYPE html>
<html lang="en">
<head>
<meta charset="utf-8">
<title>Tallowmere Vale – Enrolments Now Open</title>
<link rel="stylesheet" href="https://fonts.googleapis.com/css2?family=Oswald:wght@500;600;700&display=swap">
<style>
  :root {
    --night: #050404;
    --skin-deep: #7a4a2e;
    --skin-warm: #b9825c;
    --frame: rgba(235, 235, 235, 0.55);
    --headline: rgba(225, 225, 225, 0.82);
    --white: #ffffff;
  }
  html, body {
    margin: 0;
    padding: 0;
    width: 1200px;
    height: 1200px;
    overflow: hidden;
    background: var(--night);
  }
  .ad {
    position: relative;
    width: 1200px;
    height: 1200px;
    overflow: hidden;
    font-family: "Oswald", "Arial Narrow", sans-serif;
  }
  .ad__photo {
    position: absolute;
    inset: 0;
    background:
      radial-gradient(ellipse 70% 65% at 58% 52%, var(--skin-warm) 0%, var(--skin-deep) 38%, rgba(40, 22, 14, 0.9) 62%, var(--night) 85%);
  }
  .ad__art {
    position: absolute;
    inset: 0;
  }
  .frame {
    fill: none;
    stroke: var(--frame);
    stroke-width: 18;
  }
  .headline {
    fill: var(--headline);
    font-weight: 600;
    font-size: 222px;
    letter-spacing: 4px;
  }
  .enrol {
    fill: var(--white);
    font-weight: 600;
    font-size: 86px;
  }
  .tagline {
    fill: var(--white);
    font-weight: 500;
    font-size: 58px;
  }
  .brand__name {
    fill: var(--white);
    font-weight: 700;
    font-size: 50px;
  }
  .brand__sub {
    fill: var(--white);
    font-weight: 500;
    font-size: 19px;
  }
</style>
</head>
<body>
  <main class="ad">
    <div class="ad__photo" role="img" aria-label="Photo from above of many children's hands of different skin tones reaching together into the centre on a black background"></div>

    <svg class="ad__art" width="1200" height="1200" viewBox="0 0 1200 1200" xmlns="http://www.w3.org/2000/svg">
      <rect class="frame" x="67" y="50" width="1070" height="1070"/>

      <g class="brand">
        <text class="brand__name" x="900" y="205" text-anchor="middle" textLength="320" lengthAdjust="spacingAndGlyphs">TALLOWMERE VALE</text>
        <text class="brand__sub" x="900" y="266" text-anchor="middle" textLength="310" lengthAdjust="spacingAndGlyphs">EARLY CHILDHOOD LEARNING CENTRE</text>
      </g>

      <g class="headline-group">
        <text class="headline" x="150" y="366" textLength="665" lengthAdjust="spacingAndGlyphs">READY...</text>
        <text class="headline" x="150" y="550" textLength="800" lengthAdjust="spacingAndGlyphs">STEADY...</text>
        <text class="headline" x="150" y="737" textLength="390" lengthAdjust="spacingAndGlyphs">GO...</text>
      </g>

      <text class="enrol" x="143" y="883" textLength="932" lengthAdjust="spacingAndGlyphs">ENROLMENTS NOW OPEN</text>
      <text class="tagline" x="155" y="990" textLength="930" lengthAdjust="spacingAndGlyphs">Get your child ready for school with us!</text>
    </svg>
  </main>
</body>
</html>
```